Corporate Capability Statement for Brenwick Procurement Partners LLC

Create Corporate Capability Statement for Consulting Firm small business start-up. Minority woman-owned consulting firm based in Washington, DC metropolitan area with a target market of the local and federal government. Would like see some area government images such as buildings or monuments. Sending previous Cape Statement which really need a complete over haul. Looking for something eye-catching and creates a strong presence. The final design should communicate our numerous service offerings.

Target Market(s)

Government

Industry/Entity Type

Management Consulting

Font styles to use
Serif
Sans Serif

Requirements
Must have
• Must be able to showcase all service offerings on one-page. Usage of company colors blue and gray.
Nice to have
• images of Washington DC or government monuments illustrated in the document.
• Nice to have my contact info listed on the cape statement somewhere with the updated info below:
• Company POC: Marisa T. Holloway, CEO & Founder
• Oakmere, MD 20999 | 202.555.0147 | info@brenwickpartners-example.com | www.brenwickpartners-example.com

```html
<!DOCTYPE html>
<html lang="en">
<head>
<meta charset="utf-8">
<title>Brenwick Procurement Partners – Capabilities Statement</title>
<link rel="stylesheet" href="https://fonts.googleapis.com/css2?family=Oswald:wght@500&family=Source+Sans+3:ital,wght@0,400;0,600;1,400&display=swap">
<style>
:root{
  --blue:#2b73bd;
  --blue-deep:#1f5d9f;
  --navy:#1c4f86;
  --accent:#1e8ad8;
  --ink:#1a1a1a;
  --gray-lt:#f1f1f1;
  --gray:#dcdcdc;
  --charcoal:#222;
  --white:#fff;
}
*{margin:0;padding:0;box-sizing:border-box}
html,body{width:1200px;height:1200px;overflow:hidden;background:#fff}
body{font-family:"Source Sans 3",Arial,sans-serif;color:var(--ink)}
.sheet{position:absolute;left:152px;top:20px;width:896px;height:1160px;background:linear-gradient(180deg,#fff 0%,#f6f6f6 100%);overflow:hidden}
.abs{position:absolute}
.italic{font-style:italic}

.header-panel{left:0;top:0;width:400px;height:165px;background:linear-gradient(135deg,var(--blue-deep),var(--blue));clip-path:polygon(0 0,355px 0,388px 165px,0 165px)}
.panel-title{font-weight:600;font-size:14px;color:var(--white);text-transform:uppercase;letter-spacing:.2px}
.contact{left:50px;top:40px;color:var(--white)}
.kv{display:grid;grid-template-columns:90px 1fr;font-style:italic;font-size:12.5px;line-height:16.5px;color:var(--white)}
.contact .kv{margin-top:14px}

.capitol-image{left:380px;top:0;width:300px;height:165px;background:radial-gradient(ellipse at 45% 60%,#f3e6d3 0%,#dfe3ea 45%,#eef0f3 80%);clip-path:polygon(0 0,300px 0,300px 165px,33px 165px)}
.title{right:42px;top:26px;text-align:right;font-family:"Oswald","Arial Narrow",sans-serif;font-weight:500;line-height:44px;font-size:44px;letter-spacing:-.5px}
.title .l1{color:#111}
.title .l2{color:var(--blue)}

.rule{left:0;width:896px;height:3px;background:var(--navy)}
.tab{height:30px;border-radius:15px 0 0 15px;font-weight:600;font-size:14px;display:flex;align-items:center;justify-content:center;text-transform:uppercase}
.tab-overview{left:688px;top:145px;width:170px;background:var(--navy);color:var(--white)}
.tab-corner{width:26px;height:30px;clip-path:polygon(0 0,50% 0,100% 100%,0 100%)}

.overview{left:50px;top:188px;width:796px;font-style:italic;font-size:12.5px;line-height:16px;text-align:justify;text-align-last:right}

.info-panel{left:0;top:303px;width:430px;height:262px;background:linear-gradient(135deg,var(--blue-deep),var(--blue) 70%);clip-path:polygon(0 0,405px 0,418px 262px,0 262px)}
.info{left:50px;top:356px;color:var(--white)}
.info .kv{grid-template-columns:90px 270px;margin-top:8px;row-gap:10px}
.brand{left:250px;top:372px;width:120px;text-align:center;color:var(--white);font-size:21px;font-weight:600;letter-spacing:2px}
.brand .dot{display:block;width:40px;height:40px;border-radius:50%;background:var(--white);margin:0 auto 10px}

.naics-panel{left:0;top:565px;width:450px;height:330px;background:linear-gradient(90deg,#ececec,#f7f7f7 60%,#e4e4e4)}
.naics{left:50px;top:585px;width:360px}
.section-title{font-size:14.5px;color:var(--accent);text-transform:uppercase;font-weight:400}
.naics .kv{color:var(--ink);margin-top:8px;row-gap:10px;grid-template-columns:90px 250px}

.sic-panel{left:0;top:895px;width:400px;height:150px;background:linear-gradient(135deg,var(--blue-deep),var(--blue));clip-path:polygon(0 0,398px 0,372px 150px,0 150px)}
.sic{left:50px;top:912px;color:var(--white);font-size:13px;line-height:17px}
.sic .panel-title{margin-bottom:4px;font-weight:400;font-size:14.5px}

.services{left:477px;top:320px;width:369px;text-align:right}
.service{margin-bottom:18px}
.service h3{font-size:14.5px;font-weight:400;color:var(--accent);text-transform:uppercase;margin-bottom:4px}
.service p{font-style:italic;font-size:12.5px;line-height:16px;text-align:justify;text-align-last:right}

.tab-why{left:706px;top:1025px;width:146px;background:var(--white);border:2px solid var(--navy);color:#111;z-index:2}
.footer{left:0;top:1048px;width:896px;height:112px;background:linear-gradient(180deg,#2a2a2a,#3b3b3b 50%,#222)}
.footer p{position:absolute;left:50px;top:25px;width:796px;font-style:italic;font-size:12.5px;line-height:16px;color:var(--white);text-align:justify;text-align-last:right}
</style>
</head>
<body>
<div class="sheet">

  <div class="abs header-panel"></div>
  <div class="abs contact">
    <div class="panel-title">Company Contact</div>
    <div class="kv">
      <span>Address:</span><span>418 Harrow Creek Lane<br>Oakmere, MD 20999</span>
      <span>Phone:</span><span>(202) 555-0147</span>
      <span>Email:</span><span>mholloway@brenwickpartners-example.com</span>
    </div>
  </div>

  <div class="abs capitol-image" role="img" aria-label="Photograph of the U.S. Capitol dome against a pale sky"></div>

  <h1 class="abs title"><span class="l1">CAPABILITIES</span><br><span class="l2">STATEMENT</span></h1>

  <div class="abs rule" style="top:165px"></div>
  <div class="abs tab tab-overview">Company Overview</div>
  <div class="abs tab-corner" style="left:856px;top:145px;background:#6aa7df"></div>

  <p class="abs overview">Brenwick Procurement Partners (BPP), LLC is a woman-owned management consulting firm which provides a full suite of professional services and cutting edge solutions for government and private sector clients. We are process driven and results focused with the highest standards of ethics and integrity in all aspects of our business model. BPP’s consultants possess a significant degree of expertise and industry experience with a proven track record of providing professional excellence to our private sector and government clientele. We are dedicated to exceeding our clients’ expectations through lifecycle project management that incorporates institutional knowledge and industry best practices that will ensure the highest possible quality of end product delivery.</p>

  <div class="abs rule" style="top:300px"></div>

  <div class="abs info-panel"></div>
  <div class="abs info">
    <div class="panel-title">General Information</div>
    <div class="kv">
      <span>EIN:</span><span>Sole Source</span>
      <span>DUNS:</span><span>081947352</span>
      <span>CAGE CODE</span><span>7QKM2</span>
      <span>SET-ASIDE:</span><span>Economically Disadvantaged Woman-Owned Small Business (EDWOSB) – SBA Registered</span>
      <span>Sole Source</span><span>WOSB/EDWOSB</span>
    </div>
  </div>
  <div class="abs brand"><span class="dot"></span>BRENWICK</div>

  <div class="abs naics-panel"></div>
  <div class="abs naics">
    <div class="section-title">NAICS Codes</div>
    <div class="kv">
      <span>541210</span><span>Data Analysis and Compilation</span>
      <span>541110<br>541611</span><span>Offices of Lawyers<br>Administrative Management and General Management Consulting Services, Strategic Planning; Small Business Start-up’s</span>
      <span>541613</span><span>Marketing Consulting Services</span>
      <span>541618</span><span>Other Management Consulting Services</span>
      <span>541990</span><span>All other Professional, Scientific &amp; Technical Services; Policy &amp; Procedure Writing</span>
      <span>561410</span><span>Document Preparation Services</span>
      <span>561499</span><span>All other Business Support Services</span>
    </div>
  </div>

  <div class="abs sic-panel"></div>
  <div class="abs sic">
    <div class="panel-title">SIC Code</div>
    <div>8111 – Legal Services<br>8742 – Management Consulting Services</div>
    <div class="panel-title" style="margin-top:10px">PSC Codes</div>
    <div>R406, R408, R410, R418, R499, R704, R707, R799</div>
  </div>

  <div class="abs services">
    <div class="service"><h3>Acquisition Management</h3><p>Advisory, Acquisition Planning &amp; Strategy, Contract Cost Estimating &amp; Pricing, Contract Negotiation, Pre &amp; Post Award Contract Administration, Procurement Package Development and Contract Closeout Support.</p></div>
    <div class="service"><h3>Administrative Support</h3><p>Professional staffing support to government, public, private, and non-profit organizations providing outsourced confidential administrative and financial staff augmentation, bookkeeping, program &amp; project support, marketing and sales assistance as well as other related services.</p></div>
    <div class="service"><h3>Business Development</h3><p>Business Branding, Capture Management, Document Compilation Support, Market Research &amp; Analysis, Proposal Development &amp; Management, Prospecting &amp; Lead Generation and Small Business Commercialization.</p></div>
    <div class="service"><h3>Legal Services</h3><p>BPP also provides legal counsel offerings providing a broad range of disciplines and projects. Offerings to include; Contract Business Law, Policy Advisory, FAR/DFAR Regulations, Collections Practice, Civil Litigation Support, Dispute Resolution, and Employment Law services</p></div>
    <div class="service"><h3>Process Improvement</h3><p>Business Process Mapping &amp; Re-engineering, Change &amp; Transition Management, Quality Assurance, Risk Management &amp; Surveillance and Standard Operating Procedures, Strategic Policy &amp; Governance, Technical Writing Support.</p></div>
    <div class="service"><h3>Program Management</h3><p>Administrative Services, Federal Accounting Compliance &amp; Standards, Government Financial System Transactions &amp; Management Support, Factsheets, Technical &amp; Fiscal Business Cases, Performance Measurement, Government Infrastructure Functional Support and Independent Verification &amp; Validation (IV&amp;V), OMB Circulars and OMB Scorecard Results reporting</p></div>
  </div>

  <div class="abs tab tab-why">Why Choose Us</div>
  <div class="abs tab-corner" style="left:850px;top:1025px;background:#6aa7df;z-index:1"></div>

  <div class="abs footer">
    <p>BPP’s executive management team and consultants have a proven track record of over 50+ years’ experience in providing professional consulting services to meet our client’s specific business needs. Our extensive expertise in working alongside some of the industry’s top professionals has gained us a unique competitive edge which enables us to assist our customers… Leading them to new relationships and concrete opportunities for growth and success.</p>
  </div>

</div>
</body>
</html>
```